I need a webpage design for the following:
The website is a Niche Community for Specialists (engineers) in the Energy sector. We have a pool of elite engineers
It should be simple. We need the following:
* Home. go to ridgemark.com That's the content (plus the credits at the bottom of the page). Very simple. We only need design now!
* Thank you page. The logo at the top and "Thank you for sending your information....etc" that's it
* Register... list of questions to register
* Personal page (where the user will manage their profile)
the logo is the one in www.ridgemark.com
Look and feel
Each slider illustrates characteristics of the customer's brand and the style your logo design should communicate.

```html
<!DOCTYPE html>
<html lang="en">
<head>
<meta charset="utf-8">
<title>Ridgemark — The elite network for PowerGen freelancing specialists</title>
<link href="https://fonts.googleapis.com/css2?family=PT+Sans:wght@400;700&family=Lato:wght@400&family=Oswald:wght@300&display=swap" rel="stylesheet">
<style>
:root{
  --navy:#1b3763;
  --navy-deep:#1a3a5f;
  --ink:#22446f;
  --hero-top:#ffffff;
  --hero-bottom:#e8f0fa;
  --panel-blue:#e3eef9;
  --panel-border:#b9d1ec;
  --field-border:#c9d3de;
  --card-end:#ebebeb;
  --step-num:#dcdcdc;
  --player-top:#3b3b3b;
  --player-bottom:#1f1f1f;
  --progress:#4a86d4;
}
*{box-sizing:border-box;margin:0;padding:0}
html,body{width:1200px;height:1064px;overflow:hidden;background:#e9edf2}
body{font-family:"PT Sans",Arial,sans-serif;color:var(--ink)}
.page{position:absolute;left:0;top:0;width:1024px;height:908px;transform:scale(1.171875);transform-origin:0 0;background:#fff}
.abs{position:absolute}
.top-band{left:0;top:0;width:1024px;height:8px;background:var(--navy-deep)}
.frame-left{left:0;top:8px;width:9px;height:450px;background:#e9edf2}
.frame-right{left:1012px;top:8px;width:12px;height:450px;background:#e9edf2}
.hero{left:9px;top:8px;width:1003px;height:450px;background:linear-gradient(to bottom,var(--hero-top) 0,var(--hero-top) 100px,var(--hero-bottom) 100%)}
.hero-divider{left:0;top:458px;width:1024px;height:4px;background:#dfe5ec}
.brand{left:50px;top:24px;font-weight:700;font-size:62px;letter-spacing:-1px;color:var(--navy);line-height:1}
.login{left:331px;top:32px;width:381px;height:61px;background:var(--panel-blue);border:1px solid var(--panel-border);border-radius:3px}
.login .field{position:absolute;top:18px;width:131px;height:23px;background:#fff;border:1px solid var(--field-border);border-radius:5px;font-size:11px;color:#7a8ea8;padding:4px 10px}
.login .btn{position:absolute;left:295px;top:19px;width:67px;height:21px;background:var(--navy-deep);color:#fff;font-size:11px;border-radius:3px;text-align:center;line-height:21px}
.about-figure{left:760px;top:33px;width:40px;height:47px;background:linear-gradient(#e8c23a 0,#e8c23a 25%,#d9d9d9 25%,#8a8a8a 100%);border-radius:6px}
.about-link{left:808px;top:44px;font-size:17px;color:var(--navy)}
.tagline{left:95px;top:244px;font-family:"Lato",Arial,sans-serif;font-size:24.5px;line-height:30px;color:var(--navy)}
.player{left:473px;top:128px;width:423px;height:291px;border-radius:3px;background:linear-gradient(var(--player-top),var(--player-bottom) 90%);box-shadow:0 8px 10px -6px rgba(40,80,140,.45)}
.controls{position:absolute;left:0;bottom:0;width:100%;height:35px;background:linear-gradient(#3c3c3c,#262626);border-top:1px solid #555;border-radius:0 0 3px 3px}
.progress{position:absolute;left:35px;top:14px;width:300px;height:8px;border-radius:4px;background:#e9e9e9;overflow:hidden}
.progress span{display:block;width:119px;height:100%;background:var(--progress)}
.section-title{left:49px;top:474px;font-family:"Lato",Arial,sans-serif;font-size:19px;color:var(--navy)}
.step{width:279px;height:90px;border-radius:16px;background:linear-gradient(to right,#ffffff 10%,var(--card-end))}
.step .num{position:absolute;left:16px;top:2px;width:60px;text-align:center;font-family:"Oswald",sans-serif;font-weight:300;font-size:72px;line-height:86px;color:var(--step-num)}
.step p{position:absolute;left:85px;top:18px;width:182px;font-size:11px;line-height:18px;text-align:justify;color:var(--ink)}
.step .cta{display:block;margin-top:4px;font-weight:700;font-size:12.5px;color:var(--navy)}
.signup{left:689px;top:492px;width:323px;height:322px;background:linear-gradient(to bottom,#fff,#f5f7fa);box-shadow:-4px 6px 10px -6px rgba(0,0,0,.12)}
.signup-head{position:absolute;left:0;top:0;width:290px;height:35px;background:linear-gradient(to right,#e6edf6 60%,rgba(230,237,246,0));padding:7px 19px;font-family:"Lato",Arial,sans-serif;font-size:17px;color:var(--navy)}
.row{position:absolute;left:23px;font-size:12.5px;color:var(--navy)}
.input{position:absolute;left:96px;width:200px;height:23px;background:#fff;border:1px solid #d8dde3;border-radius:4px;font-size:10px;color:#7d8a99;padding:4px 8px}
.select-arrow{position:absolute;right:0;top:0;width:20px;height:21px;background:#e1e7ee;border-radius:0 3px 3px 0}
.file{position:absolute;left:96px;width:121px;height:20px;background:#e6e9ed;border-radius:3px;font-size:10px;color:#6d7b8c;padding:3px 9px}
.submit{position:absolute;left:97px;top:285px;width:96px;height:27px;background:var(--navy-deep);color:#fff;font-size:12px;border-radius:3px;text-align:center;line-height:27px}
.footer{left:0;top:824px;width:1024px;height:84px;background:var(--navy-deep);color:#fff;font-size:11px}
.footer .copy{position:absolute;left:34px;top:25px}
.footer nav{position:absolute;right:29px;top:27px;display:flex;gap:6px}
.footer nav span.sep{opacity:.8}
</style>
</head>
<body>
<div class="page">
  <div class="abs top-band"></div>
  <div class="abs hero"></div>
  <div class="abs frame-left"></div>
  <div class="abs frame-right"></div>
  <div class="abs hero-divider"></div>

  <header>
    <div class="abs brand">Ridgemark</div>
    <form class="abs login">
      <div class="field" style="left:16px">username</div>
      <div class="field" style="left:153px">Password</div>
      <div class="btn">LOG IN</div>
    </form>
    <div class="abs about-figure" role="img" aria-label="Illustration of an engineer in a yellow hard hat"></div>
    <div class="abs about-link">About us</div>
  </header>

  <h1 class="abs tagline" style="font-weight:400">The elite network for PowerGen<br>freelancing specialists</h1>

  <div class="abs player">
    <svg class="abs" style="left:196px;top:110px" width="26" height="36" viewBox="0 0 26 36"><path d="M0 0L26 18L0 36Z" fill="#fff"/></svg>
    <div class="controls">
      <svg class="abs" style="left:12px;top:10px" width="14" height="16" viewBox="0 0 14 16"><path d="M0 0L14 8L0 16Z" fill="#fff"/></svg>
      <div class="progress"><span></span></div>
      <svg class="abs" style="left:387px;top:10px" width="20" height="16" viewBox="0 0 20 16"><path d="M1 5H5L10 1V15L5 11H1Z" fill="#fff"/><path d="M13 4.5Q15.5 8 13 11.5M15.5 2.5Q19.5 8 15.5 13.5" stroke="#fff" stroke-width="1.6" fill="none"/></svg>
    </div>
  </div>

  <h2 class="abs section-title" style="font-weight:400">How Ridgemark Works:</h2>

  <div class="abs step" style="left:42px;top:504px"><span class="num">1</span><p>If you are a Specialist in the Power Generation sector<span class="cta">Sign Up here &nbsp;»</span></p></div>
  <div class="abs step" style="left:370px;top:504px"><span class="num">2</span><p style="left:74px;top:16px">We will verify your application and will send you an invitation to join us</p></div>
  <div class="abs step" style="left:42px;top:615px"><span class="num">3</span><p>Register using the link provided in the Ridgemark invitation.</p></div>
  <div class="abs step" style="left:371px;top:614px;width:280px"><span class="num">4</span><p style="left:74px;top:12px;width:190px">Recommend others, help us validate your experience and be ready for your first assignment via Ridgemark!</p></div>
  <div class="abs step" style="left:238px;top:718px"><span class="num">5</span><p style="left:76px;top:12px;width:191px">Invite other Specialists and increase your ranking</p></div>

  <form class="abs signup">
    <div class="signup-head">Sign Up</div>
    <span class="row" style="top:59px">First name :</span><div class="input" style="top:55px">type your name</div>
    <span class="row" style="top:97px;left:24px">Last name :</span><div class="input" style="top:93px">type your last name</div>
    <span class="row" style="top:136px;left:24px">County :</span><div class="input" style="top:132px">choose a country<span class="select-arrow"><svg width="20" height="21" viewBox="0 0 20 21"><path d="M6 8L10 12L14 8" stroke="#1a3a5f" stroke-width="2.2" fill="none"/></svg></span></div>
    <span class="row" style="top:177px">Email :</span><div class="input" style="top:173px">type your email address</div>
    <span class="row" style="top:213px">Resume :</span><div class="file" style="top:211px">choose a file brose</div>
    <span class="row" style="top:247px">or Link :</span><div class="input" style="top:243px"></div>
    <div class="submit">SUBMIT NOW</div>
  </form>

  <footer class="abs footer">
    <div class="copy">Copyright © 2012 Company Name &nbsp;| &nbsp; All right reserved</div>
    <nav><span>Home</span><span class="sep">|</span><span>About Us</span><span class="sep">|</span><span>Services</span><span class="sep">|</span><span>Log In</span><span class="sep">|</span><span>Register</span><span class="sep">|</span><span>Contact</span></nav>
  </footer>
</div>
</body>
</html>
```